Austrian finance und insurance broker needs business card design

We Need a serious looking Design for Business Card. we consult private and corporates customers in finance and insurance questions. the final design should express security and experience. We consult customers in questions of loans, Investments and insurance and have a wide range of Banks to offer. We compare several offers and select the best for our customers.

Target Market(s)

private and coporate customers with efforts in Money and insurance

Industry/Entity Type

Insurance Broker

Contact Information for Business Card

Martin Brauneder
Geschäftsführer
staatl. geprüfter Vermögensberater und Versicherungsmakler
Tel: 0664 512 8049
office@der-brauneder.at
www.der-brauneder.at
Anton Weibl Gasse 14
2135 Halbach
GISA Nr. 40527318 u. 40816493 (backside)

Font styles to use
Serif
Sans Serif

Requirements
Must have
• logo (designcrowd zip) and all Details
Nice to have
• makler logo design, maybe a 2 coloured Version is possible

```html
<!DOCTYPE html>
<html lang="de">
<head>
<meta charset="utf-8">
<title>MB Vermögensberatung – Visitenkarte</title>
<link href="https://fonts.googleapis.com/css2?family=Arimo:wght@400;700&family=Quicksand:wght@600;700&display=swap" rel="stylesheet">
<style>
  :root {
    --backdrop: #2e2e30;
    --card-white: #f3f3f3;
    --brand-blue: #1b57bd;
    --text-grey: #5a5a5a;
    --rule-grey: #6b6b6b;
    --white: #ffffff;
  }
  * { margin: 0; padding: 0; box-sizing: border-box; }
  html, body {
    width: 1200px; height: 960px; overflow: hidden;
    background: var(--backdrop);
    font-family: "Arimo", Arial, sans-serif;
  }
  .canvas { position: relative; width: 1200px; height: 960px; }

  .card {
    position: absolute;
    width: 598px; height: 342px;
    border-radius: 18px;
    overflow: hidden;
  }
  .card--front { left: 322px; top: 110px; background: var(--card-white); }
  .card--back  { left: 320px; top: 493px; background: var(--brand-blue); }

  /* front */
  .brand {
    position: absolute; left: 44px; top: 38px;
    display: flex; align-items: center; gap: 18px;
  }
  .brand__circle {
    width: 64px; height: 64px; border-radius: 50%;
    background: var(--brand-blue);
    flex: none;
  }
  .brand__text { display: flex; flex-direction: column; gap: 4px; }
  .brand__name {
    font-family: "Quicksand", sans-serif; font-weight: 700;
    font-size: 14.5px; color: var(--brand-blue);
  }
  .brand__tagline {
    font-family: "Quicksand", sans-serif; font-weight: 700;
    font-size: 10.5px; color: var(--text-grey);
  }
  .divider {
    position: absolute; left: 124px; top: 35px;
    width: 3px; height: 276px; background: var(--rule-grey);
  }
  .icon {
    position: absolute; left: 88px; width: 15px; height: 15px;
    fill: var(--brand-blue);
  }
  .person { position: absolute; left: 138px; top: 130px; }
  .person__name {
    font-size: 23px; font-weight: 700; color: var(--brand-blue);
    letter-spacing: 0.3px; line-height: 1;
  }
  .person__role {
    margin-top: 7px; margin-left: 2px;
    font-size: 14.5px; font-weight: 700; color: var(--text-grey);
  }
  .person__title {
    margin-top: 8px; margin-left: 2px;
    font-size: 12.5px; font-weight: 700; color: var(--text-grey); line-height: 1.3;
  }
  .contact {
    position: absolute; left: 140px;
    font-size: 13.5px; color: var(--text-grey); line-height: 1;
  }

  /* back */
  .back-brand {
    position: absolute; left: 0; right: 0; top: 140px;
    text-align: center;
    font-family: "Quicksand", sans-serif; font-weight: 700;
    font-size: 32px; color: var(--white);
  }
  .registration {
    position: absolute; left: 0; right: 0; top: 288px;
    text-align: center; font-size: 13.5px; font-weight: 700; color: var(--white);
  }
</style>
</head>
<body>
<main class="canvas">

  <section class="card card--front" aria-label="Vorderseite">
    <div class="brand">
      <div class="brand__circle" aria-hidden="true"></div>
      <div class="brand__text">
        <span class="brand__name">MB Vermögensberatung GmbH</span>
        <span class="brand__tagline">Finanzieren, Versichern, Vorsorgen</span>
      </div>
    </div>

    <div class="divider" aria-hidden="true"></div>

    <svg class="icon" style="top:134px" viewBox="0 0 16 16" aria-hidden="true">
      <circle cx="8" cy="4.5" r="3.5"/><path d="M1 16c0-4 3-6.5 7-6.5s7 2.5 7 6.5z"/>
    </svg>
    <div class="person">
      <div class="person__name">MARTIN BRAUNEDER</div>
      <div class="person__role">GESCHÄFTSFÜHRER</div>
      <div class="person__title">Geprüfter Vermögensberater<br>und Versicherungsmakler</div>
    </div>

    <svg class="icon" style="top:216px" viewBox="0 0 16 16" aria-hidden="true">
      <path d="M3.5 1l2.5 3-1.5 2c1 2 3 4 5 5l2-1.5 3 2.5-1.5 2.5C7 15 1 9 1 2.5z"/>
    </svg>
    <div class="contact" style="top:219px">0664 512 8049</div>

    <svg class="icon" style="top:238px" viewBox="0 0 16 16" aria-hidden="true">
      <path d="M1 3h14v10H1z" fill="none" stroke="#1b57bd" stroke-width="1.6"/><path d="M1 3l7 6 7-6" fill="none" stroke="#1b57bd" stroke-width="1.6"/>
    </svg>
    <div class="contact" style="top:239px">office@der-brauneder.at</div>

    <svg class="icon" style="top:256px" viewBox="0 0 16 16" aria-hidden="true">
      <circle cx="8" cy="8" r="7"/><path d="M1 8h14M8 1c3 3 3 11 0 14M8 1c-3 3-3 11 0 14" fill="none" stroke="#f3f3f3" stroke-width="1.2"/>
    </svg>
    <div class="contact" style="top:258px">www.der-brauneder.at</div>

    <svg class="icon" style="top:279px" viewBox="0 0 16 16" aria-hidden="true">
      <path d="M8 0a5.5 5.5 0 0 0-5.5 5.5C2.5 10 8 16 8 16s5.5-6 5.5-10.5A5.5 5.5 0 0 0 8 0zm0 8a2.5 2.5 0 1 1 0-5 2.5 2.5 0 0 1 0 5z"/>
    </svg>
    <div class="contact" style="top:282px; left:143px">Anton Weibl Gasse 14, 2135 Halbach</div>
  </section>

  <section class="card card--back" aria-label="Rückseite">
    <p class="back-brand">MB Vermögensberatung</p>
    <p class="registration">GISA Nr. 40527318 u. 40816493</p>
  </section>

</main>
</body>
</html>
```